Infection control

to re-design website to include the benefits of powdered bleach packed in pre-measured sachets which when dissolved in water provides economy, efficacy and is safe to use with the use of costly packaging. We need new text outlining the benefits of the world's most commonly used disinfectant for major hospitals, institutions, pathology, military and disaster areas.

Translate design into coded website using CMS with the following features:
Mobile responsive using HTML 5/ CSS3 standards
Coded with SEO standards and with H1 tags for easy spidering and with Wordpress CMS with is page rank 9
Site migration
Email support
Updates

Target Market(s)

hospitals, institutions, pathology, military and disaster areas

Industry/Entity Type

Chemical Product

Number of Pages Required

4 page

Colors

Designer to choose colors to be used in the design.

Requirements
Must have
• factual information based on the efficiency of sodium hypochlorite (bleach) used for infection control. The many viruses, bacteria, pathogens etc which certain strengths of bleach eliminate upon contact.
• As tis is a redesign, existing pages including MSDS sheets to stay the same
Nice to have
• a new look and feel including current logos
Should not have
• incorrect info

```html
<!DOCTYPE html>
<html lang="en">
<head>
<meta charset="utf-8">
<title>Clora-Pak 4000 – Infection Control Applications</title>
<link rel="stylesheet" href="https://fonts.googleapis.com/css2?family=Cabin:wght@500;600&display=swap">
<style>
  :root {
    --ink: #111111;
    --paper: #ffffff;
    --banner: #1f1f1f;
    --banner-fold: #4a4a4a;
    --accent: #6be01f;
    --accent-light: #b9f27a;
    --floor-top: #b8d1c4;
    --floor-bottom: #e9efe9;
    --theatre-top: #d9e4df;
    --theatre-bottom: #a8d5b4;
    --pack-top: #f4f4f4;
    --pack-bottom: #f5b335;
  }
  * { box-sizing: border-box; margin: 0; padding: 0; }
  html, body { width: 1200px; height: 1067px; overflow: hidden; background: var(--paper); }
  body { font-family: "Cabin", sans-serif; color: var(--ink); position: relative; }

  .usage-group { position: absolute; }
  .usage-group h2 { font-weight: 500; font-size: 23px; line-height: 28px; margin-bottom: 8px; }
  .usage-group ul { list-style: none; font-weight: 500; font-size: 13.6px; line-height: 15.2px; }

  .photo { position: absolute; border-radius: 4px; }
  .photo--cleaning { left: 647px; top: 0; width: 510px; height: 324px;
    background: linear-gradient(180deg, var(--floor-top) 0%, #cfe0d6 45%, var(--floor-bottom) 100%); }
  .photo--theatre { left: 46px; top: 405px; width: 510px; height: 573px;
    background: linear-gradient(180deg, var(--theatre-top) 0%, var(--theatre-bottom) 45%, #eef0ee 78%, #f2f2f2 100%); }

  .swoosh { position: absolute; }

  .product-banner { position: absolute; left: 606px; top: 398px; width: 558px; height: 58px; }
  .product-banner h1 { position: absolute; left: 0; top: 0; width: 558px; height: 43px;
    background: var(--banner); color: var(--paper); font-weight: 600; font-size: 28px;
    line-height: 43px; text-align: center; }
  .product-banner svg { position: absolute; left: 0; top: 0; }

  .pack-shot { position: absolute; left: 640px; top: 488px; width: 134px; height: 156px; border-radius: 4px;
    background: linear-gradient(180deg, var(--pack-top) 0%, var(--pack-top) 52%, var(--pack-bottom) 58%, var(--pack-bottom) 88%, var(--pack-top) 92%); }

  .product-intro { position: absolute; left: 830px; top: 497px; width: 310px;
    font-weight: 500; font-size: 13.6px; line-height: 18px; text-align: justify; }
</style>
</head>
<body>

  <section class="usage-group" style="left:68px; top:10px;">
    <h2>Infectious Wards</h2>
    <ul>
      <li>Wiping tables and bench tops</li>
      <li>Mopping floors</li>
      <li>Sanitising mattress covers</li>
      <li>Disinfecting cutlery or other implements used by infectious patients</li>
      <li>Operating Theatres</li>
    </ul>
  </section>

  <section class="usage-group" style="left:68px; top:139px;">
    <h2>Operating tables</h2>
    <ul>
      <li>Mopping floors</li>
      <li>Walls</li>
    </ul>
  </section>

  <section class="usage-group" style="left:68px; top:223px;">
    <h2>Pathology Laboratories</h2>
    <ul>
      <li>Bench tops</li>
      <li>Floors</li>
      <li>Walls</li>
    </ul>
  </section>

  <div class="photo photo--cleaning" role="img" aria-label="Cleaner in theatre scrubs mopping a glossy hospital floor"></div>
  <svg class="swoosh" style="left:832px; top:330px;" width="328" height="22" viewBox="0 0 328 22" aria-hidden="true">
    <path d="M0 1 L328 0 C326 12 318 21 302 21 C210 16 100 8 0 1 Z" fill="var(--accent)"/>
  </svg>

  <svg class="swoosh" style="left:48px; top:378px;" width="306" height="21" viewBox="0 0 306 21" aria-hidden="true">
    <path d="M306 20 L0 21 C2 9 10 0 26 0 C120 5 210 12 306 20 Z" fill="var(--accent)"/>
  </svg>
  <div class="photo photo--theatre" role="img" aria-label="Modern operating theatre with surgical lights, monitors and an operating table"></div>
  <svg class="swoosh" style="left:224px; top:986px;" width="328" height="20" viewBox="0 0 328 20" aria-hidden="true">
    <path d="M0 0 L328 0 C326 11 318 19 302 19 C210 14 100 6 0 0 Z" fill="var(--accent)"/>
  </svg>

  <header class="product-banner">
    <svg width="558" height="58" viewBox="0 0 558 58" aria-hidden="true">
      <path d="M0 43 L20 43 L20 58 Z" fill="var(--banner-fold)"/>
      <path d="M558 43 L538 43 L538 58 Z" fill="var(--banner-fold)"/>
    </svg>
    <h1>Clora-Pak 4000 ®</h1>
  </header>

  <div class="pack-shot" role="img" aria-label="Clora-Pak 4000 20 g powdered disinfectant sachet"></div>

  <p class="product-intro">Clora-Pak 4000 ® is recommended for 'dirty' areas with a high risk of infection. It is recommended for spills of blood or other body fluids, porous surfaces, benches and walls. Clora-Pak 4000 ® has been evaluated according to TGA guidelines for hospital grade disinfectant and sanitisers under dirty conditions.</p>

  <section class="usage-group" style="left:639px; top:706px;">
    <h2>Theatre</h2>
    <ul>
      <li>Blood and body fluid spills</li>
    </ul>
  </section>

  <section class="usage-group" style="left:639px; top:775px;">
    <h2>Pathology &amp; Labratories</h2>
    <ul>
      <li>Benches and surfaces involved in a spill of blood or any other body fluid</li>
      <li>Specimen containers</li>
      <li>Disinfection of hazardous waste</li>
      <li>Emergency and first aid kits</li>
    </ul>
  </section>

  <section class="usage-group" style="left:639px; top:889px;">
    <h2>Mortuary</h2>
    <ul>
      <li>Tables, Floors, walls and benches</li>
      <li>Disinfecting drains and sinks</li>
      <li>Cadavers may be washed down using solution if body fluids are present</li>
    </ul>
  </section>

</body>
</html>
```